Certificate of Completion - Educational Trainings

We are looking for a certificate of completion for individuals who complete one of our specific trainings. Files should be provided in a Word (docx) or PowerPoint (pptx) format. The "Talmoray example.png" file is to show necessary information. Copies of logos have been included for design purposes.

Target Market(s)

Training Participants

Industry/Entity Type

Healthcare

Font styles to use
Sans Serif

```html
<!DOCTYPE html>
<html lang="en">
<head>
<meta charset="utf-8">
<title>Talmoray Certificate of Completion</title>
<link rel="stylesheet" href="https://fonts.googleapis.com/css2?family=Montserrat:wght@500;700;800&family=Open+Sans:wght@400;700&family=Poppins:wght@400&family=Tinos&family=UnifrakturCook:wght@700&display=swap">
<style>
  :root {
    --band-green: #6dae51;
    --frame-green: #146b2e;
    --rule-green: #a9d29b;
    --paper: #ffffff;
    --ink: #111111;
    --seal-gold: #c9955a;
  }
  * { margin: 0; padding: 0; box-sizing: border-box; }
  html, body { width: 1200px; height: 848px; overflow: hidden; background: var(--band-green); }
  .certificate { position: relative; width: 1200px; height: 848px; background: var(--band-green); color: var(--ink); }
  .paper { position: absolute; left: 27px; top: 23px; width: 1147px; height: 800px; background: var(--paper); }
  .frame { position: absolute; left: 51px; top: 42px; width: 1098px; height: 764px; border: 2.5px solid var(--frame-green); }
  .corner { position: absolute; width: 30px; height: 30px; background: var(--frame-green); opacity: .9; }
  .corner.tl { left: 51px; top: 42px; }
  .corner.tr { left: 1119px; top: 42px; }
  .corner.bl { left: 51px; top: 776px; }
  .corner.br { left: 1119px; top: 776px; }
  .centered { position: absolute; left: 0; width: 1200px; text-align: center; }
  .brand { top: 72px; display: flex; justify-content: center; align-items: center; gap: 14px; }
  .brand-dot { width: 40px; height: 40px; border-radius: 50%; background: var(--frame-green); }
  .brand-name { font-family: "Montserrat", sans-serif; font-weight: 800; font-size: 40px; letter-spacing: 2px; color: var(--ink); line-height: 1; }
  .sponsor-line { top: 128px; font-family: "Poppins", sans-serif; font-size: 16px; letter-spacing: .2px; }
  .title { top: 152px; font-family: "UnifrakturCook", serif; font-weight: 700; font-size: 104px; letter-spacing: 17px; padding-left: 17px; line-height: 1.1; }
  .subtitle { top: 262px; font-family: "Montserrat", sans-serif; font-weight: 500; font-size: 33px; letter-spacing: 1.2px; }
  .flourish { position: absolute; left: 474px; top: 316px; width: 252px; height: 14px; border-radius: 7px;
    background: linear-gradient(90deg, rgba(109,174,81,0), rgba(109,174,81,.55) 50%, rgba(109,174,81,0)); }
  .awarded { top: 347px; font-family: "Tinos", serif; font-size: 21px; letter-spacing: 4.4px; }
  .rule { position: absolute; height: 1px; background: var(--rule-green); }
  .rule.name { left: 224px; top: 447px; width: 752px; }
  .rule.date { left: 131px; top: 680px; width: 313px; }
  .rule.signer { left: 755px; top: 679px; width: 310px; }
  .details { top: 463px; font-family: "Open Sans", sans-serif; font-size: 16.5px; letter-spacing: 2.2px; line-height: 23.6px; }
  .details .field { font-weight: 700; }
  .seal { position: absolute; left: 541px; top: 603px; width: 118px; height: 118px; border-radius: 50%; background: var(--seal-gold); }
  .sign-label { position: absolute; font-family: "Montserrat", sans-serif; font-weight: 500; font-size: 25px; line-height: 1; }
  .sign-label.date { left: 150px; top: 701px; letter-spacing: 1.4px; }
  .sign-label.signer { left: 768px; top: 697px; letter-spacing: 0.4px; }
  .footnote { top: 749px; font-family: "Poppins", sans-serif; font-size: 14.6px; line-height: 19.5px; }
</style>
</head>
<body>
<main class="certificate">
  <div class="paper"></div>
  <div class="frame"></div>
  <div class="corner tl" role="img" aria-label="Corner ornament"></div>
  <div class="corner tr" role="img" aria-label="Corner ornament"></div>
  <div class="corner bl" role="img" aria-label="Corner ornament"></div>
  <div class="corner br" role="img" aria-label="Corner ornament"></div>

  <header class="centered brand">
    <span class="brand-dot"></span>
    <span class="brand-name">TALMORAY</span>
  </header>
  <p class="centered sponsor-line">48 HARBOR LANE, STE. 310, BRIGHTWATER, ME 04190 | NATIONAL REGISTRY SPONSOR NUMBER 72318</p>

  <h1 class="centered title">Certificate</h1>
  <h2 class="centered subtitle">OF COMPLETION</h2>
  <div class="flourish" role="img" aria-label="Decorative green flourish"></div>

  <p class="centered awarded">THIS CERTIFICATE IS AWARDED TO</p>
  <div class="rule name"></div>

  <div class="centered details">
    <p>FOR SUCCESSFUL COMPLETION OF</p>
    <p>BEST PRACTICES: BUDGET PROCESS / BUDGET BUILDING</p>
    <p>COMPLETED ONLINE</p>
    <p class="field">FIELD OF STUDY FINANCE</p>
    <p>CPE CREDITS : 1</p>
  </div>

  <div class="rule date"></div>
  <p class="sign-label date">COMPLETION DATE</p>

  <div class="seal" role="img" aria-label="Gold certificate seal"></div>

  <div class="rule signer"></div>
  <p class="sign-label signer">SENIOR CONSULTANT</p>

  <footer class="centered footnote">
    <p>IN ACCORDANCE WITH THE STANDARD OF THE NATIONAL BOARD OF CPE SPONSORS,</p>
    <p>CPE CREDITS HAVE BEEN GRANTED BASED ON A 50 MINUTE HOUR.</p>
  </footer>
</main>
</body>
</html>
```